Dane Morrow films- wedding and event films company website. DESKTOP AND MOBILE

We need a website for a high-end wedding and event film production company. Looking for a very modern and elegant design. my old website is www.danemorrowfilms.example

I like the "white/black/rose gold" color scheme of my logo.

really looking for a sleek modern design the breaths professional and artistic.

Target Market(s)

wedding and event films.

Industry/Entity Type

Film Production

Number of Pages Required

5+ page

Colors

Designer to choose colors to be used in the design.

Requirements
Must have
• website name will be www.danemorrowfilms.example
• tagline is "CINEMATIC STORIES ABOUT YOU"
• sections: HOME, CONTACT, ABOUT, FILMS, BLOG
• You can see my old website at danemorrowfilms.example
• Website about section:
• Dane Morrow Films was Established with the basis of truly cinematic and artistic films in mind. Dane and his team routinely travel the globe documenting weddings and events for high profile clients and discerning couples. Dane was born and raised in Maui Hawaii and has a unique approach to his films that embody the essence of a Hollywood film. Dane has spent the last 10 years traveling the world documenting corporate events and weddings with multiple Award winning production companies. In 2017 Dane decided to establish his own brand “Dane Morrow films” that will take everything he has learned with his past experiences and push it to the next level. Aside from his personal achievements, Dane is extremely passionate about his craft and always looks forward to handcrafting beautiful wedding/event films for his clients. The style of work is non-traditional and the day of filming is extremely unobtrusive (as we are looking for natural-candid/ raw emotions).
• If you are looking for the best price in town, we are probably not the best option, but if you’re looking for the best quality and peace of mind on your wedding day, then you’re in the right place. Dane Morrow Films is a boutique studio that only accepts a limited number of assignments per year. Inquire early to ensure availability.
• LINKS TO VIMEO VIDEOS THAT WILL BE IN THE "FILMS' SECTION.
• BRENT FILM TRAILER - https://clipvault.example/508114362
• BRENT FEATURE FILM - https://clipvault.example/617392048
• JUNE AND ROB'S WEDDING - https://clipvault.example/724958160
• DRONE DEMO REEL - https://clipvault.example/841576203
• WEDDING INDUSTRY EVENT PARTY - https://clipvault.example/962304817/a8d3e7b21c
• images that you can use on site are here: https://brigittolsenimages.proofbox.example/gallery/nora&felix/
• password is: meadow

```html
<!DOCTYPE html>
<html lang="en">
<head>
<meta charset="utf-8">
<title>Blog — Dane Morrow Films</title>
<link rel="stylesheet" href="https://fonts.googleapis.com/css2?family=Oswald:wght@300;400&family=Open+Sans:wght@400;600;700&display=swap">
<style>
  :root {
    --page: #262626;
    --ink: #ffffff;
    --muted: #8a8a8a;
    --rose: #d49c6b;
    --rose-line: #8a6b4c;
    --band-dark: #1e1e1e;
    --band-mid: #2b2b2b;
    --top-band: #232323;
    --footer: #1a1a1a;
    --head-font: "Oswald", sans-serif;
    --body-font: "Open Sans", sans-serif;
  }
  * { box-sizing: border-box; margin: 0; padding: 0; }
  html, body { width: 1200px; height: 2293px; overflow: hidden; }
  body { background: var(--page); color: var(--ink); font-family: var(--body-font); position: relative; }

  .hero { position: absolute; left: 0; top: 0; width: 1200px; height: 624px; overflow: hidden; }
  .hero-photo { position: absolute; inset: 0;
    background:
      radial-gradient(ellipse 330px 200px at 600px 380px, #3a342e 0%, rgba(30,26,22,0) 100%),
      linear-gradient(180deg, #0b0b0b 0%, #141211 50%, #2a1f15 78%, #3a2a1b 100%); }
  .brand { position: absolute; left: 87px; top: 38px; display: flex; align-items: center; gap: 8px;
    font-family: var(--body-font); font-weight: 600; font-size: 11px; letter-spacing: 1.5px; color: var(--ink); text-transform: uppercase; }
  .brand-mark { width: 10px; height: 10px; background: var(--rose); }
  .main-nav { position: absolute; top: 37px; left: 0; width: 1200px; }
  .main-nav a { position: absolute; font-family: var(--head-font); font-size: 13px; letter-spacing: 1px;
    color: var(--ink); text-decoration: none; }
  .main-nav a.is-current { color: var(--rose); }
  .hero-title { position: absolute; left: 0; width: 1200px; top: 280px; text-align: center;
    font-family: var(--head-font); font-weight: 300; font-size: 46px; letter-spacing: 4px; }

  .section-title { position: absolute; left: 87px; top: 666px; font-family: var(--head-font);
    font-weight: 300; font-size: 29px; letter-spacing: 2px; }

  .post { position: absolute; left: 89px; width: 1022px; height: 304px; border: 1.5px solid var(--rose-line); }
  .post-badge { position: absolute; left: -12px; top: -2px; width: 64px; height: 29px; background: var(--rose);
    color: #1d1d1d; font-family: var(--head-font); font-size: 14px; letter-spacing: 1.5px;
    display: flex; align-items: center; justify-content: center; }
  .post-photo { position: absolute; left: 35px; top: 38px; width: 227px; height: 227px; }
  .post-title { position: absolute; left: 301px; top: 124px; font-weight: 700; font-size: 16px; }
  .post-excerpt { position: absolute; left: 301px; top: 165px; width: 680px; font-size: 12.5px; line-height: 16px; }
  .post-more { position: absolute; left: 857px; top: 232px; width: 127px; height: 31px; background: var(--rose);
    color: #1d1d1d; font-size: 13px; letter-spacing: 1px; display: flex; align-items: center; justify-content: center; text-decoration: none; }

  .pager { position: absolute; left: 1072px; top: 1692px; font-size: 13px; letter-spacing: 1px; }

  .gallery { position: absolute; left: 0; top: 1733px; width: 1200px; height: 404px; display: flex; }
  .gallery-item { width: 400px; height: 404px; background: var(--band-dark); }
  .gallery-item.is-mid { background: var(--band-mid); }
  .gallery-photo { width: 400px; height: 282px; }
  .gallery-caption { padding: 28px 36px 0; font-size: 13.5px; line-height: 16px; letter-spacing: 1px; }
  .gallery-arrow { position: absolute; top: 1860px; width: 14px; height: 34px; background: #3a3a3a;
    display: flex; align-items: center; justify-content: center; font-size: 12px; }

  .back-to-top { position: absolute; left: 0; top: 2137px; width: 1200px; height: 52px; background: var(--top-band);
    display: flex; align-items: center; justify-content: center; color: var(--rose); font-size: 13px; letter-spacing: 2px; text-decoration: none; }

  .site-footer { position: absolute; left: 0; top: 2189px; width: 1200px; height: 104px; background: var(--footer); }
  .copyright { position: absolute; left: 87px; top: 44px; font-size: 12.5px; color: #666; }
  .footer-brand { position: absolute; left: 0; width: 1200px; top: 44px; display: flex; justify-content: center; align-items: center; gap: 8px;
    font-weight: 600; font-size: 11px; letter-spacing: 1.5px; text-transform: uppercase; }
  .social { position: absolute; top: 46px; width: 12px; height: 12px; border-radius: 50%; background: #5c5c5c; }
</style>
</head>
<body>
  <header class="hero">
    <div class="hero-photo" role="img" aria-label="Vintage film camera on a dark wooden table"></div>
    <div class="brand"><span class="brand-mark"></span>Dane Morrow Films</div>
    <nav class="main-nav">
      <a href="#" style="left:722px">HOME</a>
      <a href="#" style="left:803px">ABOUT</a>
      <a href="#" class="is-current" style="left:890px">FILMS</a>
      <a href="#" style="left:978px">CONTACT</a>
      <a href="#" style="left:1082px">BLOG</a>
    </nav>
    <h1 class="hero-title">BLOG</h1>
  </header>

  <h2 class="section-title">BLOG</h2>

  <article class="post" style="top:751px">
    <span class="post-badge">NEW</span>
    <div class="post-photo" role="img" aria-label="Silver rangefinder camera on dark background" style="background:linear-gradient(135deg,#1c1f22,#3a3e42 55%,#15181a)"></div>
    <h3 class="post-title">Basics of Photography: The Complete Guide</h3>
    <p class="post-excerpt">We spent the last week learning all about the basics of photography, from the way your camera works to composing your photos to editing them in post. Here's the complete guide, along with a PDF of all the lessons and some additional resources fo learning more.</p>
    <a class="post-more" href="#">Read More</a>
  </article>

  <article class="post" style="top:1062px">
    <div class="post-photo" role="img" aria-label="Close-up of a camera lens and lens cap" style="background:radial-gradient(circle at 35% 45%,#2e3a36 0%,#111 55%,#1c1c1c 100%)"></div>
    <h3 class="post-title">Basics of Photography: The Complete Guide</h3>
    <p class="post-excerpt">We spent the last week learning all about the basics of photography, from the way your camera works to composing your photos to editing them in post. Here's the complete guide, along with a PDF of all the lessons and some additional resources fo learning more.</p>
    <a class="post-more" href="#">Read More</a>
  </article>

  <article class="post" style="top:1373px">
    <div class="post-photo" role="img" aria-label="Close-up of a camera lens and lens cap" style="background:radial-gradient(circle at 35% 45%,#2e3a36 0%,#111 55%,#1c1c1c 100%)"></div>
    <h3 class="post-title">Basics of Photography: The Complete Guide</h3>
    <p class="post-excerpt">We spent the last week learning all about the basics of photography, from the way your camera works to composing your photos to editing them in post. Here's the complete guide, along with a PDF of all the lessons and some additional resources fo learning more.</p>
    <a class="post-more" href="#">Read More</a>
  </article>

  <div class="pager">1/5 &nbsp;&gt;</div>

  <section class="gallery">
    <div class="gallery-item">
      <div class="gallery-photo" role="img" aria-label="Camera lens resting on dry pine needles" style="background:radial-gradient(circle at 48% 55%,#5a6a6a 0%,#2a2622 45%,#4a3522 100%)"></div>
      <p class="gallery-caption">Lorem Ipsum is simply dummy text of the printing and typesetting industry.</p>
    </div>
    <div class="gallery-item is-mid">
      <div class="gallery-photo" role="img" aria-label="White off-road vehicle on a snowy plain at sunrise" style="background:linear-gradient(180deg,#c9cdd6 0%,#e8d9c6 40%,#b9c3cf 60%,#dde3ea 100%)"></div>
      <p class="gallery-caption">Lorem Ipsum is simply dummy text of the printing and typesetting industry.</p>
    </div>
    <div class="gallery-item">
      <div class="gallery-photo" role="img" aria-label="Camera floating above an open hand in the dark" style="background:radial-gradient(circle at 55% 45%,#2a3038 0%,#0d0f12 70%)"></div>
      <p class="gallery-caption">Lorem Ipsum is simply dummy text of the printing and typesetting industry.</p>
    </div>
  </section>
  <span class="gallery-arrow" style="left:0">&lt;</span>
  <span class="gallery-arrow" style="left:1186px">&gt;</span>

  <a class="back-to-top" href="#">BACK TO TOP</a>

  <footer class="site-footer">
    <p class="copyright">Copyright by DANE MORROW &nbsp;© 2015</p>
    <div class="footer-brand"><span class="brand-mark"></span>Dane Morrow Films</div>
    <a class="social" href="#" aria-label="Social profile" style="left:962px"></a>
    <a class="social" href="#" aria-label="Social profile" style="left:1034px"></a>
    <a class="social" href="#" aria-label="Video profile" style="left:1099px"></a>
  </footer>
</body>
</html>
```